Brightpath Learning Data Dashboard

Brightpath Learning is a leading provider of digital curriculum and online courses to increase educational opportunities and achievement to students in grades K-12. Teachers and students access all course materials online.

School districts need greater visibility into the rate in which students are progressing through their courses, so school staff can better support students to complete courses at the required rate to keep them on track for graduation.
This can be accomplished by allowing school administrators to view a data dashboard and pull an on-demand report and see progress for a specified date range, relative to overall progress.

Within a specified date range, school administrators want to know if the student made more or less progress than in the period prior to the first date in the range.
School administrators also want to know if students are ahead or behind where they should be after the second date in the range.

Industry/Entity Type

Digital

```html
<!DOCTYPE html>
<html lang="en">
<head>
<meta charset="utf-8">
<title>Brightpath Learning – Time Based Performance</title>
<link href="https://fonts.googleapis.com/css2?family=Roboto:wght@400;500;700&display=swap" rel="stylesheet">
<style>
:root{
  --brand:#5a4f93;
  --brand-dark:#4a3f80;
  --ink-purple:#3b3270;
  --side-light:#ebe8f7;
  --side-mid:#d6d1ec;
  --text:#222;
  --line:#dcdcdc;
  --field-bg:#fff;
  --field-btn:#d7d7d7;
  --menu-bg:#f0f0f0;
  --footer:#000;
}
*{box-sizing:border-box;margin:0;padding:0}
html,body{width:1200px;height:506px;overflow:hidden;background:#fff;font-family:"Roboto",Arial,sans-serif;color:var(--text)}
.app{position:relative;width:1200px;height:506px}
.topbar{position:absolute;left:0;top:0;width:1200px;height:60px;background:var(--brand)}
.menu-toggle{position:absolute;left:0;top:0;width:46px;height:60px;background:var(--brand-dark);display:flex;align-items:center;justify-content:center}
.brand-name{position:absolute;left:60px;top:22px;color:#fff;font-size:13px;font-weight:500;letter-spacing:.3px}
.user{position:absolute;left:610px;top:13px;display:flex;align-items:center;gap:7px;color:#fff;font-size:10.5px}
.avatar{width:34px;height:34px;border-radius:50%;background:radial-gradient(circle at 50% 40%,#c99a7a,#7a4a2e)}
.user-menu{position:absolute;left:648px;top:36px;width:88px;background:var(--menu-bg);box-shadow:0 1px 3px rgba(0,0,0,.2);font-size:8px;color:#333}
.user-menu div{height:20px;line-height:20px;padding-left:11px}
.user-menu div+div{background:#e6e6e6}
.sidebar{position:absolute;left:0;top:60px;width:46px;height:420px;background:linear-gradient(var(--side-light),#e2def4)}
.side-nav{background:var(--side-mid);height:40px;display:flex;align-items:center;justify-content:center;border-bottom:1px solid #c9c3e2}
.side-user{height:40px;display:flex;align-items:center;justify-content:center;border-bottom:1px solid #d5d0ea}
.page-title{position:absolute;left:74px;top:81px;font-size:17.5px;font-weight:400;color:#222}
.download{position:absolute;left:555px;top:80px;width:147px;height:23px;background:#3d3470;color:#fff;font-size:11px;letter-spacing:1.6px;font-weight:500;display:flex;align-items:center;justify-content:center}
.filter{position:absolute;top:119px;width:147px}
.filter-label{font-size:9.6px;color:#333;height:15px;position:relative;display:flex;align-items:center}
.radio-opt{position:absolute;top:0;height:15px;display:flex;align-items:center;gap:4px}
.radio{display:inline-block;width:7px;height:7px;border-radius:50%;border:1.5px solid var(--ink-purple)}
.radio.on{background:var(--ink-purple)}
.select{height:24px;border:1px solid #e0e0e0;background:var(--field-bg);font-size:8px;color:#555;display:flex;align-items:center;padding-left:11px;position:relative;box-shadow:0 1px 2px rgba(0,0,0,.08)}
.select .caret{position:absolute;right:0;top:0;width:20px;height:22px;background:var(--field-btn);display:flex;align-items:center;justify-content:center}
.data-table{position:absolute;left:74px;top:179px;width:1097px;border-collapse:collapse;table-layout:fixed;font-size:8.2px}
.data-table th,.data-table td{border:1px solid var(--line);padding:0 0 0 10px;text-align:left;vertical-align:middle}
.data-table th{color:var(--ink-purple);font-weight:700;font-size:7.6px;text-transform:uppercase;letter-spacing:.3px;line-height:1.3}
.data-table th.group{text-align:center;padding:0;font-size:8.8px;color:#222}
.data-table th.sub{text-align:center;padding:0;color:#222}
.data-table th.sub.small{color:var(--ink-purple)}
.data-table td{height:30.4px;color:#222}
.data-table td.ctr{text-align:center;padding:0}
.scrollbar{position:absolute;left:74px;top:455px;width:1098px;height:12px;background:#eee;border:1px solid #bbb}
.scroll-thumb{position:absolute;left:46px;top:1px;width:130px;height:8px;background:#c8c8c8;border:1px solid #999}
.scroll-btn{position:absolute;top:1px;width:7px;height:8px}
.footer{position:absolute;left:0;top:480px;width:1200px;height:26px;background:var(--footer);color:#fff;font-size:7.8px;display:flex;align-items:center;padding-left:289px}
</style>
</head>
<body>
<div class="app">
  <header class="topbar">
    <div class="menu-toggle">
      <svg width="18" height="13" viewBox="0 0 18 13"><g stroke="#fff" stroke-width="1.5"><line x1="0" y1="1" x2="18" y2="1"/><line x1="0" y1="6.5" x2="18" y2="6.5"/><line x1="0" y1="12" x2="18" y2="12"/></g></svg>
    </div>
    <div class="brand-name">Brightpath Learning</div>
    <div class="user">
      <div class="avatar" role="img" aria-label="User profile photo"></div>
      <span>Jane Doe</span>
      <svg width="7" height="5" viewBox="0 0 7 5"><path d="M1 1l2.5 2.5L6 1" stroke="#fff" fill="none" stroke-width="1.2"/></svg>
    </div>
  </header>
  <div class="user-menu"><div>My Profile</div><div>Log Out</div></div>

  <nav class="sidebar">
    <div class="side-nav">
      <svg width="14" height="11" viewBox="0 0 14 11"><path d="M1.5 10A6 6 0 1 1 12.5 10" fill="none" stroke="#3d3470" stroke-width="2"/><line x1="7" y1="8" x2="9.5" y2="4" stroke="#3d3470" stroke-width="1.6"/></svg>
    </div>
    <div class="side-user">
      <svg width="11" height="12" viewBox="0 0 11 12"><circle cx="5.5" cy="3" r="3" fill="#3d3470"/><path d="M0 12a5.5 4.5 0 0 1 11 0z" fill="#3d3470"/></svg>
    </div>
  </nav>

  <h1 class="page-title">Time Based Performance</h1>
  <div class="download">DOWNLOAD FILE</div>

  <div class="filter" style="left:74px"><div class="filter-label">School:</div><div class="select">Choose a school...<span class="caret"><svg width="6" height="4" viewBox="0 0 6 4"><path d="M.5.5L3 3 5.5.5" stroke="#777" fill="none"/></svg></span></div></div>
  <div class="filter" style="left:234px"><div class="filter-label"><span class="radio-opt" style="left:0"><span class="radio"></span>Observer:</span><span class="radio-opt" style="left:88px"><span class="radio on"></span>Teacher:</span></div><div class="select">Choose an observer...<span class="caret"><svg width="6" height="4" viewBox="0 0 6 4"><path d="M.5.5L3 3 5.5.5" stroke="#777" fill="none"/></svg></span></div></div>
  <div class="filter" style="left:394px"><div class="filter-label">Filter Date 1:</div><div class="select">2/27/18<span class="caret"><svg width="6" height="4" viewBox="0 0 6 4"><path d="M.5.5L3 3 5.5.5" stroke="#777" fill="none"/></svg></span></div></div>
  <div class="filter" style="left:555px"><div class="filter-label">Filter date 2:</div><div class="select">3/6/18<span class="caret"><svg width="6" height="4" viewBox="0 0 6 4"><path d="M.5.5L3 3 5.5.5" stroke="#777" fill="none"/></svg></span></div></div>

  <table class="data-table">
    <colgroup>
      <col style="width:84px"><col style="width:70px"><col style="width:58px"><col style="width:90px"><col style="width:59px"><col style="width:48px"><col style="width:54px"><col style="width:54px"><col style="width:62px"><col style="width:51px"><col style="width:63px"><col style="width:52px"><col style="width:64px"><col style="width:79px"><col style="width:85px"><col style="width:78px"><col style="width:46px">
    </colgroup>
    <thead>
      <tr style="height:18px">
        <th rowspan="3">Student Name</th><th rowspan="3">Observer</th><th rowspan="3">School</th><th rowspan="3">Course Title</th><th rowspan="3">Current Grade</th><th rowspan="3">Raw Score</th><th rowspan="3">Course Start Date</th><th rowspan="3">Course End Date</th>
        <th colspan="4" class="group">PERCENT COMPLETE</th>
        <th rowspan="3">2/27-3/6 Progress Actual/ Goal</th><th rowspan="3">Status as of March 6</th><th rowspan="3">Completion Rate / Day for the Range</th><th rowspan="3" style="text-align:center;padding:0">Completion Rate Change</th><th rowspan="3">Last Login</th>
      </tr>
      <tr style="height:17px"><th colspan="2" class="sub">START - 2/27/18</th><th colspan="2" class="sub">END - 3/6/18</th></tr>
      <tr style="height:18px"><th class="sub small">ACTUAL %</th><th class="sub small">GOAL %</th><th class="sub small">ACTUAL %</th><th class="sub small">GOAL %</th></tr>
    </thead>
    <tbody>
      <tr><td>Adrian Walsh</td><td>Ben Hale</td><td>Maplecrest</td><td>Algebra 1A</td><td>67.3%</td><td>70%</td><td>2/20/18</td><td>4/24/18</td><td>0%</td><td>10%</td><td>5%</td><td>20%</td><td>5/10</td><td>5/20</td><td>.2%</td><td class="ctr"><svg width="8" height="11" viewBox="0 0 8 11"><path d="M4 11V1M1 4l3-3 3 3" stroke="#2d2660" stroke-width="1.4" fill="none"/></svg></td><td>3/6/18</td></tr>
      <tr><td>Leo Fenwick</td><td>Ben Hale</td><td>Maplecrest</td><td>Biology A</td><td>74.2%</td><td>83%</td><td>2/20/18</td><td>4/24/18</td><td>5%</td><td>10%</td><td>15%</td><td>20%</td><td>10/10</td><td>15/20</td><td>2.28%</td><td class="ctr"><svg width="8" height="11" viewBox="0 0 8 11"><path d="M4 11V1M1 4l3-3 3 3" stroke="#2d2660" stroke-width="1.4" fill="none"/></svg></td><td>3/6/18</td></tr>
      <tr><td>Nina Park</td><td>Rosa Valdemar</td><td>Harwood</td><td>US History A</td><td>82.3%</td><td>82.3%</td><td>2/20/18</td><td>4/24/18</td><td>15%</td><td>10%</td><td>20%</td><td>20%</td><td>5/10</td><td>20/20</td><td>7.14%</td><td class="ctr"><svg width="8" height="11" viewBox="0 0 8 11"><path d="M4 0v10M1 7l3 3 3-3" stroke="#2d2660" stroke-width="1.4" fill="none"/></svg></td><td>3/3/18</td></tr>
      <tr><td>Dylan Brooks</td><td>Rosa Valdemar</td><td>Harwood</td><td>Algebra 1A</td><td>91.0%</td><td>95.0%</td><td>2/20/18</td><td>4/24/18</td><td>9%</td><td>10%</td><td>11%</td><td>20%</td><td>2/10</td><td>11/20</td><td>5%</td><td class="ctr"><svg width="8" height="11" viewBox="0 0 8 11"><path d="M4 0v10M1 7l3 3 3-3" stroke="#2d2660" stroke-width="1.4" fill="none"/></svg></td><td>3/3/18</td></tr>
      <tr><td>Mateo Delgardo</td><td>Amy Portwell</td><td>Elmsford</td><td>Language Arts 10 A</td><td>94.5%</td><td>94.5%</td><td>2/20/18</td><td>4/24/18</td><td>11%</td><td>10%</td><td>28%</td><td>20%</td><td>17/10</td><td>28/20</td><td>2.8%</td><td class="ctr"><svg width="8" height="11" viewBox="0 0 8 11"><path d="M4 11V1M1 4l3-3 3 3" stroke="#2d2660" stroke-width="1.4" fill="none"/></svg></td><td>3/2/18</td></tr>
      <tr><td>Ethan Revel</td><td>Amy Portwell</td><td>Elmsford</td><td>Language Arts 10B</td><td>80%</td><td>85%</td><td>2/20/18</td><td>4/24/18</td><td>5%</td><td>10%</td><td>10%</td><td>20%</td><td>5/10</td><td>10/20</td><td>3%</td><td class="ctr"><svg width="16" height="8" viewBox="0 0 16 8"><path d="M1 4h14M4 1L1 4l3 3M12 1l3 3-3 3" stroke="#2d2660" stroke-width="1.4" fill="none"/></svg></td><td>3/2/18</td></tr>
      <tr><td>Clara Minton</td><td>Amy Portwell</td><td>Elmsford</td><td>US History 1A</td><td>75%</td><td>80%</td><td>2/20/18</td><td>4/24/18</td><td>10%</td><td>10%</td><td>20%</td><td>20%</td><td>10/10</td><td>20/20</td><td>.2%</td><td class="ctr"><svg width="16" height="8" viewBox="0 0 16 8"><path d="M1 4h14M4 1L1 4l3 3M12 1l3 3-3 3" stroke="#2d2660" stroke-width="1.4" fill="none"/></svg></td><td>3/5/18</td></tr>
    </tbody>
  </table>

  <div class="scrollbar">
    <svg class="scroll-btn" style="left:2px" viewBox="0 0 7 8"><path d="M6 0v8L1 4z" fill="#111"/></svg>
    <div class="scroll-thumb"></div>
    <svg class="scroll-btn" style="right:2px" viewBox="0 0 7 8"><path d="M1 0v8l5-4z" fill="#111"/></svg>
  </div>

  <footer class="footer">Brightpath Learning © 2018&nbsp;&nbsp;|&nbsp;&nbsp;All Rights Reserved.</footer>
</div>
</body>
</html>
```